Business Card & Word Docs from existing Logo

We need a business card with typical information plus layout to include electrical contractors license number, VORLE license and KMT license. We would like a word document layout for a proposal document, opening page with logo and design basic information; proposal to and proposal from and project name and number. Small basic single page letter for general documents. Email signature with logo.

We are an electrical, refrigeration and automation contractor. We work with reducing energy consumption for our customers and complex process solutions in electrical, refrigeration and automation.
Updates

Reason: Final changes/ revisions to designs.

Target Market(s)

Industrial and commercial businesses that require more than your average contractor.

Industry/Entity Type

Electrical

Requirements
Must have
• Propsal document must have a full opening page.

```html
<!DOCTYPE html>
<html lang="en">
<head>
<meta charset="utf-8">
<title>Kelvara Contracting – Business Card</title>
<link href="https://fonts.googleapis.com/css2?family=Source+Sans+3:wght@400;600&display=swap" rel="stylesheet">
<style>
  :root {
    --backdrop: #e9e6e2;
    --card-white: #ffffff;
    --navy: #1d4f86;
    --ink: #2a2a2a;
    --teal-blue: #1a86b4;
    --teal-green: #139a4e;
    --watermark: #ececec;
  }
  * { box-sizing: border-box; margin: 0; padding: 0; }
  html, body { width: 1200px; height: 900px; overflow: hidden; }
  body {
    background: var(--backdrop);
    font-family: "Source Sans 3", "Myriad Pro", Arial, sans-serif;
    position: relative;
  }
  .card {
    position: absolute;
    top: 180px;
    width: 288px;
    height: 502px;
    border-radius: 18px;
    overflow: hidden;
    box-shadow: 0 2px 6px rgba(0,0,0,0.18);
  }
  .card--front { left: 286px; background: var(--card-white); }
  .card--back {
    left: 628px;
    background: linear-gradient(215deg, var(--teal-green) 0%, #168a7e 45%, var(--teal-blue) 100%);
    color: #fff;
  }
  .brand { position: absolute; left: 0; right: 0; text-align: center; }
  .brand__mark { display: block; margin: 0 auto; }
  .brand__name { font-weight: 600; letter-spacing: -0.5px; line-height: 1; }
  .brand__tagline { font-weight: 400; letter-spacing: 4.5px; line-height: 1; }

  .card--front .brand { top: 28px; }
  .card--front .brand__name { color: var(--navy); font-size: 32px; margin-top: 14px; }
  .card--front .brand__tagline { color: var(--ink); font-size: 15px; margin-top: 6px; padding-left: 4px; }

  .watermark { position: absolute; left: 30px; top: 230px; }

  .contact { position: absolute; left: 38px; top: 289px; color: var(--ink); }
  .contact__name { color: var(--navy); font-weight: 600; font-size: 15px; line-height: 18px; }
  .contact__role { color: var(--navy); font-size: 14.5px; line-height: 19px; }
  .contact__address { font-size: 13.5px; margin-top: 14px; line-height: 18px; }
  .contact__list { list-style: none; margin-top: 6px; }
  .contact__list li { display: flex; align-items: center; gap: 5px; font-size: 13.5px; line-height: 17.8px; }
  .contact__list svg { width: 14px; height: 14px; flex: none; }
  .licences { position: absolute; left: 38px; top: 467px; font-size: 8.5px; line-height: 11px; color: var(--ink); }

  .card--back .brand { top: 116px; }
  .card--back .brand__name { font-size: 38px; margin-top: 26px; }
  .card--back .brand__tagline { font-size: 16px; letter-spacing: 5.5px; margin-top: 9px; padding-left: 5px; }
  .card--back .web { position: absolute; left: 0; right: 0; top: 473px; text-align: center; font-size: 11px; letter-spacing: 2.4px; }
</style>
</head>
<body>

  <section class="card card--front" aria-label="Business card front">
    <svg class="watermark" width="260" height="300" viewBox="0 0 260 300" aria-hidden="true">
      <circle cx="140" cy="150" r="150" fill="var(--watermark)"/>
    </svg>

    <div class="brand">
      <svg class="brand__mark" width="72" height="72" viewBox="0 0 72 72" aria-hidden="true">
        <circle cx="36" cy="36" r="34" fill="var(--teal-blue)"/>
      </svg>
      <div class="brand__name">KELVARA</div>
      <div class="brand__tagline">CONTRACTING</div>
    </div>

    <div class="contact">
      <div class="contact__name">Daniel Hart</div>
      <div class="contact__role">Director</div>
      <div class="contact__address">PO Box 5678, Townsville, Qld, 4810</div>
      <ul class="contact__list">
        <li><svg viewBox="0 0 14 14" aria-label="Phone"><path d="M1 5c0-2 3-3 6-3s6 1 6 3l-3 1-1-2H5L4 6zM3 7h8l1 5H2z" fill="var(--navy)"/></svg>07 4821 9036</li>
        <li><svg viewBox="0 0 14 14" aria-label="Fax"><path d="M4 1h6v4H4zM1 6h12v6H1zM3 8h8v2H3z" fill="var(--navy)"/></svg>07 4821 9037</li>
        <li><svg viewBox="0 0 14 14" aria-label="Mobile"><rect x="4" y="1" width="6" height="12" rx="1" fill="var(--navy)"/><rect x="5" y="3" width="4" height="5" fill="#fff"/></svg>0417 552 908</li>
        <li><svg viewBox="0 0 14 14" aria-label="Email"><rect x="1" y="3" width="12" height="8" fill="none" stroke="var(--navy)" stroke-width="1.4"/><path d="M1 3l6 5 6-5" fill="none" stroke="var(--navy)" stroke-width="1.4"/></svg>daniel@kelvara.com.au</li>
        <li><svg viewBox="0 0 14 14" aria-label="Website"><circle cx="7" cy="7" r="5.8" fill="none" stroke="var(--navy)" stroke-width="1.4"/><path d="M1 7h12M7 1v12M3 3.5q4 2 8 0M3 10.5q4-2 8 0" fill="none" stroke="var(--navy)" stroke-width="1.1"/></svg>www.kelvara.com.au</li>
      </ul>
    </div>

    <div class="licences">
      Electrical Contractors License 12345<br>
      KMT 1234567&nbsp;&nbsp;&nbsp;VORLE AA12345
    </div>
  </section>

  <section class="card card--back" aria-label="Business card back">
    <div class="brand">
      <svg class="brand__mark" width="180" height="180" viewBox="0 0 180 180" aria-hidden="true">
        <circle cx="90" cy="90" r="84" fill="none" stroke="#fff" stroke-width="9"/>
      </svg>
      <div class="brand__name">KELVARA</div>
      <div class="brand__tagline">CONTRACTING</div>
    </div>
    <div class="web">www.kelvara.com.au</div>
  </section>

</body>
</html>
```